We are opening a new restaurant concept called Lanternleaf - Fresh Asian Cuisine. Will be a trendy, casual dining restaurant (somewhat similar to a RJ Wexleys).
I have included pics of our logo in different formats and a picture of our front menu cover and inside menu as well as our actual menu in draft format. Need 6 individual pages total and letter size. Inside cover would be a "about us" type page that describes who we are and mission statement of restaurant (script unwritten at this time), Next page would be appetizers, inside page would have entrees on left and right side of book, then noodles/rice, vegetarian, kids and dessert section, last page would be drink/cocktail menu (still in progress).

```html
<!DOCTYPE html>
<html lang="en">
<head>
<meta charset="utf-8">
<title>Lanternleaf - Fresh Asian Cuisine · Appetizer Menu</title>
<link rel="stylesheet" href="https://fonts.googleapis.com/css2?family=Oswald:wght@500;600&family=Open+Sans:wght@400&display=swap">
<style>
  :root {
    --backdrop: #e3e3e6;
    --page: #0c0c0c;
    --accent: #e1222b;
    --ink: #e8e8e8;
    --ink-soft: #bdbdbd;
    --greens: #6f8f3c;
    --greens-dark: #2f3b22;
    --plate: #9aa3ad;
  }
  * { box-sizing: border-box; margin: 0; padding: 0; }
  html, body { width: 1200px; height: 838px; overflow: hidden; }
  body { background: var(--backdrop); position: relative; }

  .spread { position: absolute; left: 20px; top: 19px; width: 1160px; height: 800px; display: flex; gap: 0; }
  .page { position: relative; width: 580px; height: 800px; background: var(--page); overflow: hidden; }
  .page--left { border-right: 1px solid #222; }

  .photo { position: absolute; border-radius: 50%; }
  .photo--edamame { left: 330px; top: -90px; width: 230px; height: 230px;
    background: radial-gradient(circle at 45% 55%, #8fae4e 0%, var(--greens) 35%, #5b4a38 60%, var(--plate) 72%, #6c7580 100%); }
  .photo--rice { left: -130px; top: 300px; width: 300px; height: 300px;
    background: radial-gradient(circle at 60% 50%, #d9cfb6 0%, #b9ad8e 35%, #3f6b2c 55%, #6d7884 72%, #4a525c 100%); }
  .photo--rolls { left: 420px; top: 110px; width: 240px; height: 240px;
    background: radial-gradient(circle at 40% 50%, #e7b04a 0%, #d9574a 25%, #e9e2d6 48%, #7aa55a 62%, #f1f1f1 74%, #c9c9c9 100%); }
  .photo--shrimp { left: 400px; top: 610px; width: 240px; height: 240px;
    background: radial-gradient(circle at 45% 40%, #c97a5a 0%, #8a4a3a 30%, #3f5a30 50%, #f2f2f2 66%, #d6d6d6 100%); }

  .dot { position: absolute; left: 418px; top: 158px; width: 54px; height: 54px; border-radius: 50%;
    background: var(--accent); border: 3px solid #fff; }

  .section-title { position: absolute; left: 230px; top: 178px;
    font: 600 30px/1 "Oswald", sans-serif; letter-spacing: 3px; color: var(--accent); }

  .menu-list { position: absolute; list-style: none; }
  .page--left .menu-list { left: 230px; top: 236px; width: 310px; }
  .page--right .menu-list { left: 48px; top: 120px; width: 360px; }

  .menu-item { margin-bottom: 17px; }
  .menu-item__head { display: flex; justify-content: space-between; align-items: baseline; gap: 10px; }
  .menu-item__name { font: 500 14px/1.2 "Oswald", sans-serif; letter-spacing: 0.6px; color: var(--accent); text-transform: uppercase; }
  .menu-item__price { font: 500 13px/1.2 "Oswald", sans-serif; color: var(--accent); }
  .menu-item__desc { font: 400 10.5px/1.45 "Open Sans", sans-serif; color: var(--ink-soft); margin-top: 3px; max-width: 280px; }
</style>
</head>
<body>
  <main class="spread">
    <section class="page page--left" aria-label="Appetizer page">
      <div class="photo photo--edamame" role="img" aria-label="Bowl of edamame and mushrooms with lime"></div>
      <div class="dot"></div>
      <div class="photo photo--rice" role="img" aria-label="Plate of rice with greens and chicken"></div>
      <h1 class="section-title">APPETIZER</h1>
      <ul class="menu-list">
        <li class="menu-item"><div class="menu-item__head"><span class="menu-item__name">Edamame</span><span class="menu-item__price">$6</span></div><p class="menu-item__desc">Steamed soybeans tossed with sea salt and lime</p></li>
        <li class="menu-item"><div class="menu-item__head"><span class="menu-item__name">Crab Rangoon</span><span class="menu-item__price">$8</span></div><p class="menu-item__desc">Crispy wontons filled with crab and cream cheese</p></li>
        <li class="menu-item"><div class="menu-item__head"><span class="menu-item__name">Lettuce Wraps</span><span class="menu-item__price">$11</span></div><p class="menu-item__desc">Minced chicken, water chestnuts and shiitake, crisp lettuce</p></li>
        <li class="menu-item"><div class="menu-item__head"><span class="menu-item__name">Salt &amp; Pepper Calamari</span><span class="menu-item__price">$10</span></div><p class="menu-item__desc">Lightly battered squid with chili and scallion</p></li>
        <li class="menu-item"><div class="menu-item__head"><span class="menu-item__name">Spicy Tuna Crisps</span><span class="menu-item__price">$12</span></div><p class="menu-item__desc">Seared rice cakes topped with spicy tuna</p></li>
        <li class="menu-item"><div class="menu-item__head"><span class="menu-item__name">Chili Garlic Wings</span><span class="menu-item__price">$11</span></div><p class="menu-item__desc">Wok-tossed wings in sweet chili garlic glaze</p></li>
        <li class="menu-item"><div class="menu-item__head"><span class="menu-item__name">Shrimp Tempura</span><span class="menu-item__price">$10</span></div><p class="menu-item__desc">Light crispy shrimp with ginger dipping sauce</p></li>
        <li class="menu-item"><div class="menu-item__head"><span class="menu-item__name">Dynamite Shrimp</span><span class="menu-item__price">$9</span></div><p class="menu-item__desc">Tempura shrimp in creamy sriracha sauce</p></li>
      </ul>
    </section>

    <section class="page page--right" aria-label="Appetizer page continued">
      <div class="photo photo--rolls" role="img" aria-label="Fresh spring rolls with dipping sauce"></div>
      <div class="photo photo--shrimp" role="img" aria-label="Bowl of shrimp with greens"></div>
      <ul class="menu-list">
        <li class="menu-item"><div class="menu-item__head"><span class="menu-item__name">Crispy Ginger Beef</span><span class="menu-item__price">$10</span></div><p class="menu-item__desc">Flash-fried beef strips with ginger, scallion and sesame</p></li>
        <li class="menu-item"><div class="menu-item__head"><span class="menu-item__name">Crispy Salt &amp; Pepper Tofu</span><span class="menu-item__price">$8</span></div><p class="menu-item__desc">Golden tofu with chili, garlic and green onion</p></li>
        <li class="menu-item"><div class="menu-item__head"><span class="menu-item__name">Steamed Chicken Dumplings (6)</span><span class="menu-item__price">$8</span></div><p class="menu-item__desc">Chicken, cabbage and mushroom served with soy vinegar</p></li>
        <li class="menu-item"><div class="menu-item__head"><span class="menu-item__name">Pork Dumplings (6)</span><span class="menu-item__price">$8</span></div><p class="menu-item__desc">Pan-seared pork dumplings with chili oil</p></li>
        <li class="menu-item"><div class="menu-item__head"><span class="menu-item__name">Pork Egg Rolls (2)</span><span class="menu-item__price">$7</span></div><p class="menu-item__desc">Hand rolled with cabbage and sweet plum sauce</p></li>
        <li class="menu-item"><div class="menu-item__head"><span class="menu-item__name">Vegetable Spring Rolls (2)</span><span class="menu-item__price">$6</span></div><p class="menu-item__desc">Crisp vegetables wrapped in rice paper with peanut dip</p></li>
        <li class="menu-item"><div class="menu-item__head"><span class="menu-item__name">Garlic Cucumber Salad</span><span class="menu-item__price">$6</span></div><p class="menu-item__desc">Smashed cucumber with garlic, sesame and rice vinegar</p></li>
        <li class="menu-item"><div class="menu-item__head"><span class="menu-item__name">Lanternleaf Hot N Sour Soup</span><span class="menu-item__price">$7</span></div><p class="menu-item__desc">Tofu, bamboo shoots, mushroom and egg ribbons</p></li>
        <li class="menu-item"><div class="menu-item__head"><span class="menu-item__name">Wonton Soup</span><span class="menu-item__price">$7</span></div><p class="menu-item__desc">Pork wontons in light broth with bok choy</p></li>
      </ul>
    </section>
  </main>
</body>
</html>
```